" Nossa empresa presta serviços na área de atividade física outdoor e em condomínios para grupos de pessoas que queiram praticar atividade física funcional e bravolan. Também realizamos eventos de competiçao em Bravolan e realizamos cursos para profissionais da área de Ed. Física dentro do tema. "

```html
<!DOCTYPE html>
<html lang="pt-BR">
<head>
<meta charset="utf-8">
<title>Pulso Movement Studio — Pasta institucional</title>
<link href="https://fonts.googleapis.com/css2?family=Exo+2:wght@600&family=Roboto:wght@400&display=swap" rel="stylesheet">
<style>
  :root {
    --backdrop: #e9e8e6;
    --paper: #f4f4f4;
    --paper-shade: #e6e6e6;
    --band-gray: #8e8f91;
    --accent-green: #8cc63f;
    --ink: #4a4b4d;
    --slot-line: #5d5e60;
    --fold-shadow: rgba(0,0,0,0.08);
  }
  html, body {
    margin: 0;
    padding: 0;
    width: 1200px;
    height: 1200px;
    overflow: hidden;
    background: var(--backdrop);
  }
  .canvas {
    position: relative;
    width: 1200px;
    height: 1200px;
  }
  .folder-spread {
    position: absolute;
    left: 96px;
    top: 108px;
    width: 1008px;
    height: 984px;
    box-shadow: 0 6px 18px rgba(0,0,0,0.18);
  }
  .folder-spread svg {
    position: absolute;
    inset: 0;
    display: block;
  }
  .page-texture {
    position: absolute;
    top: 0;
    width: 504px;
    height: 984px;
    background: linear-gradient(160deg, var(--paper) 0%, var(--paper-shade) 55%, var(--paper) 100%);
  }
  .page-texture.left { left: 0; }
  .page-texture.right { left: 504px; }
  .brand-mark {
    position: absolute;
    right: 66px;
    top: 432px;
    text-align: right;
    font-family: "Exo 2", sans-serif;
    font-weight: 600;
    color: var(--ink);
    line-height: 1;
  }
  .brand-mark .brand-name {
    display: block;
    font-size: 74px;
    letter-spacing: 4px;
  }
  .brand-mark .brand-line {
    display: block;
    margin-top: 8px;
    font-size: 17px;
    letter-spacing: 5.5px;
  }
  .contact-block {
    position: absolute;
    left: 300px;
    top: 798px;
    display: flex;
    align-items: flex-start;
    gap: 8px;
    font-family: "Roboto", sans-serif;
    font-size: 6px;
    line-height: 9px;
    color: var(--ink);
  }
  .contact-block .contact-brand {
    font-family: "Exo 2", sans-serif;
    font-weight: 600;
    font-size: 9px;
    letter-spacing: 1px;
    padding-top: 10px;
  }
  .contact-block ul {
    list-style: none;
    margin: 0;
    padding: 0;
  }
</style>
</head>
<body>
<main class="canvas">
  <section class="folder-spread">
    <div class="page-texture left" role="img" aria-label="Padrão suave de losangos cinza-claro sobre o papel"></div>
    <div class="page-texture right" role="img" aria-label="Padrão suave de losangos cinza-claro sobre o papel"></div>

    <svg viewBox="0 0 1008 984" width="1008" height="984" aria-hidden="true">
      <!-- left page corner bands -->
      <polygon class="band-gray" points="0,0 88,0 0,275" fill="var(--band-gray)"/>
      <polygon class="band-green" points="98,0 114,0 0,356 0,306" fill="var(--accent-green)"/>
      <!-- right page corner bands -->
      <polygon class="band-green" points="1008,600 1008,640 898,984 882,984" fill="var(--accent-green)"/>
      <polygon class="band-gray" points="1008,652 1008,984 902,984" fill="var(--band-gray)"/>
      <!-- centre fold -->
      <rect class="fold" x="498" y="0" width="12" height="984" fill="var(--fold-shadow)"/>
      <!-- card slots -->
      <path class="card-slot" d="M504,264 A24,24 0 0 1 504,312" fill="none" stroke="var(--slot-line)" stroke-width="1.5"/>
      <path class="card-slot" d="M504,636 A24,24 0 0 1 504,684" fill="none" stroke="var(--slot-line)" stroke-width="1.5"/>
    </svg>

    <div class="contact-block">
      <ul>
        <li>Rua das Palmeiras 120</li>
        <li>São Paulo SP</li>
        <li>(11) 5555-0142</li>
        <li>contato@pulsomove.com.br</li>
      </ul>
      <span class="contact-brand">PULSO</span>
    </div>

    <div class="brand-mark">
      <span class="brand-name">PULSO</span>
      <span class="brand-line">MOVEMENT STUDIO</span>
    </div>
  </section>
</main>
</body>
</html>
```